Business card design needed

Quiet Haven Network is a not-for- profit organisation which advocates for palliative care in the community and runs a good size volunteer program to the community. We also run day hospice centres, provide massage & podiatry to clients etc. Our current business cards are very old fashioned and a new look is timely to some positive changes bringing the organisation forward.
Updates

Hi everyone, Thank you all so much for submitting your very clever designs.  I will confer with my colleagues tomorrow and hopefully we can make a decision :)

Industry/Entity Type

Massage

Contact Information for Business Card

Miriam Coley
Operations Manager
T 02 6180 4392
M 0417552864
E Miriam@quiethavennet.org.au

Logo Text

Quiet Haven Network Inc

Logo styles of interest
Pictorial/Combination Logo
Requirements
Must have
• Our logo (I think I have attached it, contact me if it didn't work)

```html
<!DOCTYPE html>
<html lang="en">
<head>
<meta charset="utf-8">
<title>Quiet Haven Network – Business Card</title>
<link rel="stylesheet" href="https://fonts.googleapis.com/css2?family=Open+Sans:wght@400&family=Tinos:wght@400&display=swap">
<style>
  :root {
    --backdrop: #e6e5e2;
    --card: #ffffff;
    --maroon: #8c1f45;
    --ink: #1e1e1e;
    --mark: #f2c930;
    --shadow: rgba(0,0,0,0.22);
  }
  * { margin: 0; padding: 0; box-sizing: border-box; }
  html, body {
    width: 1200px; height: 998px; overflow: hidden;
    background: var(--backdrop);
  }
  .stage { position: relative; width: 1200px; height: 998px; }
  .card {
    position: absolute; left: 160px; width: 880px; height: 440px;
    background: var(--card);
    box-shadow: 0 6px 18px var(--shadow);
    overflow: hidden;
  }
  .card--front { top: 40px; }
  .card--back { top: 518px; }

  .brand-mark {
    position: absolute; display: flex; align-items: center; gap: 10px;
    font-family: "Tinos", serif; font-size: 20px; color: var(--maroon);
  }
  .brand-mark .dot {
    width: 22px; height: 22px; border-radius: 50%; background: var(--mark);
  }
  .org-name {
    position: absolute;
    font-family: "Tinos", serif; color: var(--maroon);
  }

  .card--front .brand-mark { left: 70px; top: 90px; }
  .card--front .org-name { left: 70px; top: 200px; font-size: 24px; }
  .card--front .photo {
    position: absolute; right: 0; top: 0; width: 520px; height: 100%;
    background: radial-gradient(ellipse at 55% 50%, #8a5a3a 0%, #c9a583 35%, #f3eee8 70%, #ffffff 100%);
  }

  .card--back .left {
    position: absolute; left: 0; top: 0; width: 400px; height: 100%;
  }
  .card--back .brand-mark { left: 90px; top: 50px; }
  .card--back .org-name { left: 100px; top: 140px; font-size: 19px; }
  .person {
    position: absolute; left: 80px; top: 185px;
    font-family: "Open Sans", sans-serif; color: var(--maroon);
  }
  .person .name { font-size: 28px; line-height: 1.2; }
  .person .role { font-size: 22px; line-height: 1.2; }
  .contacts {
    position: absolute; left: 60px; top: 300px;
    font-family: "Open Sans", sans-serif; font-size: 18px; line-height: 1.45;
    border-collapse: collapse;
  }
  .contacts th { color: var(--maroon); font-weight: 400; text-align: left; padding-right: 14px; }
  .contacts td { color: var(--ink); }
  .card--back .photo {
    position: absolute; right: 0; top: 0; width: 480px; height: 100%;
    background: linear-gradient(120deg, #d8c3a0 0%, #c39a7c 40%, #e9c6b4 60%, #5b5048 100%);
  }
</style>
</head>
<body>
<main class="stage">
  <section class="card card--front">
    <div class="brand-mark"><span class="dot"></span>Quiet Haven Network</div>
    <p class="org-name">Quiet Haven Network Inc.</p>
    <div class="photo" role="img" aria-label="Spa still life with bath salts, soap, towel, candle and green leaves"></div>
  </section>

  <section class="card card--back">
    <div class="left">
      <div class="brand-mark"><span class="dot"></span>Quiet Haven Network</div>
      <p class="org-name">Quiet Haven Network Inc.</p>
      <div class="person">
        <p class="name">Miriam Coley</p>
        <p class="role">Operations Manager</p>
      </div>
      <table class="contacts">
        <tr><th>Tell:</th><td>02 6180 4392</td></tr>
        <tr><th>Mobile:</th><td>0417552864</td></tr>
        <tr><th>Email:</th><td>Miriam@quiethavennet.org.au</td></tr>
      </table>
    </div>
    <div class="photo" role="img" aria-label="Feet resting on smooth massage stones with white daisies"></div>
  </section>
</main>
</body>
</html>
```